Book Cover - For Best Selling Diet

Hi
Book cover required for a diet book being marketed to become a best seller
For best quality, image will be 2820 pixels on the shortest side and 4500 pixels on the longest side .
The book name : Bright Morning Plan
By Marisol Penhale
( will add in the extra text once we see design - top and bottom subtitle )
I do not want a photo of a person on the book.
PLEASE SEE " THE NINE STEP CORE" by Dale Whitcombe as an example of solid style and I also love Quiet Lantern for the font.
Branding Colours:
#F26432
#A4195C
#A7D8CC
Font that runs through our brand is : helvetica neue
This is for a book that will be marketed for #1 bestseller - So please only quality
designs that are designed in a unique style.
Thanks
Target Market(s)
Busy Working Mums, Affluent, 30+ .
Look and feel

```html
<!DOCTYPE html>
<html lang="en">
<head>
<meta charset="utf-8">
<title>Bright Morning Plan — Marisol Penhale</title>
<link rel="stylesheet" href="https://fonts.googleapis.com/css2?family=Roboto+Condensed:wght@500&family=Roboto:wght@400&display=swap">
<style>
  :root {
    --orange: #F26432;
    --magenta: #A4195C;
    --magenta-bright: #B3206A;
    --mint: #A7D8CC;
    --ink-on-band: #F26432;
  }
  * { margin: 0; padding: 0; box-sizing: border-box; }
  html, body {
    width: 1004px;
    height: 1200px;
    overflow: hidden;
    background: var(--mint);
  }
  .cover {
    position: absolute;
    left: 152px;
    top: 42px;
    width: 700px;
    height: 1116px;
    background: var(--orange);
    overflow: hidden;
    color: var(--magenta-bright);
    font-family: "Roboto", "Helvetica Neue", Arial, sans-serif;
  }
  .kicker,
  .subtitle {
    position: absolute;
    left: 0;
    width: 100%;
    text-align: center;
    font-size: 19px;
    line-height: 26px;
    letter-spacing: 0.2px;
  }
  .kicker { top: 48px; }
  .title {
    position: absolute;
    left: 0;
    width: 100%;
    text-align: center;
    font-family: "Roboto Condensed", "Helvetica Neue", Arial, sans-serif;
    font-weight: 500;
    color: var(--magenta-bright);
    line-height: 1;
  }
  .title-line-small {
    display: block;
    margin-top: 112px;
    font-size: 78px;
    letter-spacing: 1px;
  }
  .title-line-large {
    display: block;
    margin-top: -8px;
    font-size: 232px;
    letter-spacing: 2px;
    line-height: 0.92;
  }
  .rule {
    position: absolute;
    left: 152px;
    top: 410px;
    width: 428px;
    height: 10px;
    background: var(--mint);
  }
  .subtitle { top: 430px; }
  .figure-area {
    position: absolute;
    left: 200px;
    top: 506px;
    width: 210px;
    height: 460px;
    border-radius: 90px 90px 20px 20px;
    background: var(--magenta);
  }
  .author-band {
    position: absolute;
    left: 0;
    top: 966px;
    width: 100%;
    height: 82px;
    background: var(--magenta);
    display: flex;
    align-items: center;
    justify-content: center;
  }
  .author {
    font-family: "Roboto Condensed", "Helvetica Neue", Arial, sans-serif;
    font-weight: 500;
    font-size: 52px;
    letter-spacing: 1px;
    color: var(--ink-on-band);
  }
  .blurb {
    position: absolute;
    left: 90px;
    top: 1056px;
    width: 520px;
    text-align: center;
    font-size: 12.5px;
    line-height: 16px;
    color: var(--magenta);
  }
</style>
</head>
<body>
  <main class="cover">
    <p class="kicker">Donec vitae erat molestie, gravida velit eget,<br>lacinia leo. Vivamus ac erat augue. Curabitur</p>
    <h1 class="title">
      <span class="title-line-small">BRIGHT MORNING</span>
      <span class="title-line-large">PLAN</span>
    </h1>
    <div class="rule"></div>
    <p class="subtitle">Vivamus at lacus sit amet tortor viverra eges-<br>tas id sed turpis. Nulla tincidunt ante vel susci-</p>
    <div class="figure-area" role="img" aria-label="Silhouette of a woman walking in heels, in magenta"></div>
    <div class="author-band">
      <p class="author">MARISOL PENHALE</p>
    </div>
    <p class="blurb">Donec vitae erat molestie, gravida velit eget, lacinia leo. Vivamus ac erat augue. Curabitur quis turpis id purus ultricies consequat ac eu nibh. Aenean tincidunt, libero a condimentum posuere, lectus odio aliquam ligula, at aliquet nulla libero et massa.</p>
  </main>
</body>
</html>
```